Shop window posters and banners for a contact lens (Carlow&Birkett Velora Pro)

Please take a look at our appearance on Instagram (optique_valmire), where you can also see the shop windows. In this case we would like to advertise a specific contact lens in the shop window. For this we need a poster and a banner. I can send you pictures of the lens. The poster banner should be filled with questions such as: Are you already wearing High Quality? Does your lens also have a blue filter? Feel good even after wearing it for a long time? Make an appointment with our vision experts!

Target Market(s)

Reach people who are dissatisfied with their contact lenses at the end of the day. For whom it may be important to protect their eyes from blue light.

Requirements
Must have
• correspond to the style of the store

```html
<!DOCTYPE html>
<html lang="de">
<head>
<meta charset="utf-8">
<title>Velora Pro – Schaufensterplakat</title>
<link rel="stylesheet" href="https://fonts.googleapis.com/css2?family=Abel&family=Cinzel:wght@700&display=swap">
<style>
  :root {
    --bg-dark: #b8afa1;
    --bg-mid: #d5cec3;
    --bg-light: #f2eee8;
    --ink: #1b1a19;
    --band-dark: #8f877c;
    --band-light: #d3ccc1;
    --white: #ffffff;
    --rule: #3a3835;
  }
  html, body {
    margin: 0;
    padding: 0;
    overflow: hidden;
  }
  .poster {
    position: relative;
    width: 855px;
    height: 1200px;
    overflow: hidden;
    background: linear-gradient(135deg, var(--bg-dark) 0%, var(--bg-mid) 45%, var(--bg-light) 80%, #ede8e0 100%);
    color: var(--ink);
  }
  .question {
    position: absolute;
    margin: 0;
    line-height: 1;
  }
  .question-lead {
    display: block;
    font-family: "Abel", sans-serif;
    font-size: 31px;
    font-weight: 400;
  }
  .question-key {
    display: block;
    font-family: "Cinzel", serif;
    font-weight: 700;
    font-size: 57px;
    margin-top: 10px;
  }
  .question-filter { left: 66px; top: 139px; }
  .question-comfort { left: 126px; top: 355px; }
  .cta-band {
    position: absolute;
    left: 124px;
    top: 620px;
    width: 731px;
    height: 185px;
    border-radius: 92px 0 0 92px;
    background: linear-gradient(90deg, var(--band-dark) 0%, #a39b90 45%, var(--band-light) 100%);
  }
  .cta-text {
    position: absolute;
    left: 193px;
    top: 660px;
    margin: 0;
    color: var(--white);
    line-height: 1;
  }
  .cta-lead {
    display: block;
    font-family: "Abel", sans-serif;
    font-size: 51px;
    letter-spacing: 0.5px;
  }
  .cta-key {
    display: block;
    font-family: "Cinzel", serif;
    font-weight: 700;
    font-size: 46px;
    margin-top: 10px;
  }
  .contact {
    position: absolute;
    left: 292px;
    top: 1042px;
    height: 110px;
    border-left: 1px solid var(--rule);
    padding-left: 24px;
    font-family: "Abel", sans-serif;
    font-size: 16.5px;
    letter-spacing: 1.8px;
    line-height: 22.6px;
    color: var(--ink);
  }
  .contact p { margin: 0; }
</style>
</head>
<body>
  <main class="poster">
    <h2 class="question question-filter">
      <span class="question-lead">Hat Ihre Linse auch</span>
      <span class="question-key">Blaufilter?</span>
    </h2>
    <h2 class="question question-comfort">
      <span class="question-lead">Gutes Gefühl auch nach</span>
      <span class="question-key">langem Tragen?</span>
    </h2>
    <div class="cta-band"></div>
    <h1 class="cta-text">
      <span class="cta-lead">MACHEN SIE EINEN TERMIN MIT</span>
      <span class="cta-key">Unseren Sehexperten!</span>
    </h1>
    <address class="contact">
      <p>Montags: 14:00 - 18:00</p>
      <p>Dienstag - Samstag: 09:00-18:00</p>
      <p>Telefonnummer: 00352/618290</p>
      <p>ovalmire@mail.lu</p>
      <p>optiquevalmire.shop</p>
    </address>
  </main>
</body>
</html>
```